Poster for a new "Pizza Roll" Combo at our bakery

We are a cinnamon roll and coffee focused bakery, but we would like an innovative poster design to bring attention to our new offering, a Pizza Roll. We will be offering it as a combo, and this is what we wish to advertise. It will be geared mainly towards a younger high school aged crowd. I have included pics of the Pizza Rolls, but it's up to you how you want to incorporate them in the design.Poster should include our logo, the pizza rolls, and can include a drink to illustrate the combo as well. ( we offer710 ml vimo bottle products and tulo bottled waters)Main Text: Try our amazing new Pizza Rolls! Message to get accross: $6.00 for a Pizza Roll and drink.Small Print: Avail after 11am, while supplies last. Includes one pizza roll and one bottled drink of choice. Taxes extra.

Target Market(s)

Broad, but mainly high school aged kids

Industry/Entity Type

Bakery

Colors

Designer to choose colors to be used in the design.

Requirements
Must have
• Text: " Try our amazing new PIzza Rolls!:
• $6 Pizza Roll Combo (Pizza Roll and a drink)
Nice to have
• Pic of the PIzza Roll (photo shopped if needed to improve esthetics)
• Pic of a Bottled 710ml vimo drink
Should not have
• Any animal product references, as we are a Vegan shop.

```html
<!DOCTYPE html>
<html lang="en">
<head>
<meta charset="utf-8">
<title>Pizza Roll Combo Poster</title>
<link rel="stylesheet" href="https://fonts.googleapis.com/css2?family=Archivo:ital,wght@0,800;0,900;1,800;1,900&display=swap">
<style>
  :root {
    --orange: #f7941d;
    --orange-deep: #e87a0c;
    --blue: #1c8fe6;
    --blue-band: #2ea3f2;
    --black: #111111;
    --white: #ffffff;
    --toast-light: #f3c98a;
    --toast-mid: #d99a4e;
    --toast-dark: #a9642a;
  }
  * { margin: 0; padding: 0; box-sizing: border-box; }
  html, body { width: 800px; height: 1200px; overflow: hidden; background: #ffffff; }
  .poster {
    position: relative;
    width: 800px;
    height: 1200px;
    overflow: hidden;
    font-family: "Archivo", "Arial Black", sans-serif;
  }
  .backdrop-photo {
    position: absolute; inset: 0;
    background:
      radial-gradient(ellipse at 25% 20%, var(--toast-light) 0%, transparent 55%),
      radial-gradient(ellipse at 80% 70%, #f0b870 0%, transparent 50%),
      linear-gradient(160deg, var(--toast-mid) 0%, #e8b36f 45%, var(--toast-dark) 100%);
  }
  .band {
    position: absolute;
    transform: skewX(-10deg);
  }
  .band--orange { background: var(--orange); }
  .band--white { background: var(--white); }
  .headline {
    position: absolute;
    font-weight: 900;
    font-style: italic;
    line-height: 1;
    white-space: nowrap;
    letter-spacing: -3px;
    paint-order: stroke fill;
  }
  .headline--try { left: 40px; top: 120px; font-size: 122px; color: var(--white); -webkit-text-stroke: 14px var(--black); }
  .headline--our { left: 44px; top: 268px; font-size: 92px; color: var(--black); }
  .headline--new { left: 214px; top: 228px; font-size: 146px; color: var(--blue); -webkit-text-stroke: 10px var(--white); }
  .headline--amazing { left: 56px; top: 348px; font-size: 134px; color: var(--orange); -webkit-text-stroke: 10px var(--black); }
  .headline--rolls { left: 56px; top: 478px; font-size: 138px; font-weight: 800; color: var(--orange); -webkit-text-stroke: 10px var(--black); letter-spacing: -6px; }
  .exclaim {
    position: absolute; left: 640px; top: 40px;
    font-size: 500px; font-weight: 900; font-style: italic; line-height: 1;
    color: var(--orange-deep); -webkit-text-stroke: 12px var(--black); paint-order: stroke fill;
  }
  .info-band {
    position: absolute; left: -20px; top: 640px; width: 860px; height: 100px;
    background: var(--blue-band);
    transform: rotate(-2.5deg);
  }
  .fine-print {
    position: absolute; left: 152px; top: 652px; width: 640px;
    color: var(--white); font-weight: 800; font-size: 22px; line-height: 1.55;
    transform: rotate(-2.5deg);
  }
  .drink-photo {
    position: absolute; left: 26px; top: 592px; width: 96px; height: 200px;
    border-radius: 30px 30px 14px 14px;
    background: linear-gradient(90deg, #3a0e0e 0%, #7a1a14 35%, #c2231d 50%, #5a1010 80%, #2a0707 100%);
  }
  .brand-mark {
    position: absolute; left: 625px; top: 735px; width: 140px; height: 140px;
    border-radius: 50%; background: var(--black);
    display: flex; align-items: center; justify-content: center;
  }
  .brand-name { color: var(--white); font-weight: 800; font-size: 26px; }
  .plus-sign {
    position: absolute; left: 58px; top: 852px;
    font-size: 70px; font-weight: 900; color: var(--orange-deep);
    -webkit-text-stroke: 6px var(--white); paint-order: stroke fill;
  }
  .roll-photo {
    position: absolute; left: -30px; top: 820px; width: 500px; height: 420px;
    border-radius: 48% 52% 0 0;
    background: radial-gradient(circle at 50% 45%, #f6dfb0 0%, #e8b777 35%, #c98542 70%, #a35f2c 100%);
  }
  .price-dollar {
    position: absolute; left: 458px; top: 870px;
    font-size: 78px; font-weight: 900; font-style: italic; color: var(--orange);
    -webkit-text-stroke: 8px var(--white); paint-order: stroke fill;
  }
  .price-amount {
    position: absolute; left: 468px; top: 860px;
    font-size: 330px; font-weight: 900; font-style: italic; line-height: 1; color: var(--orange);
    -webkit-text-stroke: 12px var(--white); paint-order: stroke fill;
  }
  .combo-label {
    position: absolute; right: 22px; top: 918px; text-align: right;
    font-size: 64px; font-weight: 900; line-height: 0.98; color: var(--black);
    -webkit-text-stroke: 8px var(--orange); paint-order: stroke fill;
  }
  .combo-note {
    position: absolute; right: 20px; top: 1132px;
    font-size: 25px; font-weight: 900; color: var(--black);
    -webkit-text-stroke: 5px var(--white); paint-order: stroke fill;
  }
</style>
</head>
<body>
<main class="poster">
  <div class="backdrop-photo" role="img" aria-label="Softly blurred photo of golden baked pizza rolls"></div>

  <div class="band band--orange" style="left:20px; top:134px; width:620px; height:112px;"></div>
  <div class="band band--white" style="left:20px; top:252px; width:610px; height:100px;"></div>
  <div class="band band--white" style="left:20px; top:362px; width:600px; height:106px;"></div>
  <div class="band band--white" style="left:34px; top:484px; width:660px; height:126px;"></div>

  <h1>
    <span class="headline headline--try">Try out</span>
    <span class="headline headline--our">our</span>
    <span class="headline headline--new">new</span>
    <span class="headline headline--amazing">amazing</span>
    <span class="headline headline--rolls">Pizza Rolls</span>
  </h1>
  <span class="exclaim">!</span>

  <div class="info-band"></div>
  <p class="fine-print">Available after 11am, while supplies last. Includes one pizza roll and one bottled drink of choice. Taxes extra.</p>
  <div class="drink-photo" role="img" aria-label="Photo of a 710 ml vimo cola bottle"></div>

  <div class="brand-mark"><span class="brand-name">Crumbly</span></div>

  <div class="roll-photo" role="img" aria-label="Close-up photo of a baked pizza roll swirl"></div>
  <span class="plus-sign">+</span>

  <span class="price-dollar">$</span>
  <span class="price-amount">6</span>
  <p class="combo-label">pizza<br>roll<br>combo</p>
  <p class="combo-note">(pizza roll and a drink)</p>
</main>
</body>
</html>
```